依頼詳細
店頭上部の大看板のデザインをお願いしたくおもいます。
明るく、一人でも入りやすいデザインが希望です。
記載項目
大看板サイズ:横4880×縦1280
記載項目:屋号(ゆめポリス) 390円カツ丼 カウンター10席

希望イメージ
シンプル 複雑
単色 カラフル
暗い 明るい
日常 高級
遊び心 厳粛
未来的 伝統的
女性的 男性的
希望する色
赤 黄 オレンジ やまぶき色
納品ファイル
• 高解像度JPG (.jpg)
• イラストレーター形式 (.ai)
• フォトショップ形式 (.psd)
補足説明
右下の赤い線で囲まれた部分は既存店舗(2階)への入り口になります。
また最上部にある恐竜の絵はそのまま残します。
■ 選んだ理由

皆様たくさんのご提案ありがとうございました。
どれもすばらしいものばかりでとても迷いましたが、

客単価の安い価格帯の店である為、入りやすさという事をを
多角的に検討した結果このデザインを選ばしていただきました。

今回はありがとうございました。

また機会があればよろしくお願いします。

■ 提案者全員のお礼・コメント

提案してくれたランサーの皆様ありがとうございました。
とても気に入るデザインを見つけることができました。

又運営のスタッフ様もありがとうございました。

```html
<!DOCTYPE html>
<html lang="ja">
<head>
<meta charset="utf-8">
<title>ゆめポリス 店頭大看板</title>
<link rel="stylesheet" href="https://fonts.googleapis.com/css2?family=Dela+Gothic+One&family=M+PLUS+Rounded+1c:wght@800&display=swap">
<style>
  :root {
    --bg: #eeeeee;
    --sign-red: #e60012;
    --sign-deep: #a3000c;
    --sign-top: #2a1a1a;
    --yellow: #ffd800;
    --white: #ffffff;
    --black: #141414;
  }
  * { margin: 0; padding: 0; box-sizing: border-box; }
  html, body { width: 846px; height: 1200px; overflow: hidden; background: var(--bg); }
  .canvas { position: relative; width: 846px; height: 1200px; }
  .signboard {
    position: absolute; left: 0; top: 489px; width: 846px; height: 222px;
    background: var(--sign-red);
    border-top: 8px solid var(--sign-top);
    border-bottom: 8px solid var(--sign-deep);
    font-family: "M PLUS Rounded 1c", sans-serif;
    font-weight: 800;
    overflow: hidden;
  }
  .seat-badge {
    position: absolute; left: 22px; top: 22px; width: 162px; height: 162px;
    border-radius: 50%; background: var(--sign-deep);
    border: 6px solid var(--white);
    display: flex; flex-direction: column; align-items: center; justify-content: center;
    color: var(--white); text-align: center; line-height: 1.05;
    white-space: nowrap;
  }
  .seat-badge .label {
    background: var(--yellow); color: var(--sign-red);
    font-size: 17px; padding: 2px 8px; border-radius: 4px;
  }
  .seat-badge .count { color: var(--yellow); font-size: 40px; margin: 2px 0; }
  .seat-badge .count small { font-size: 26px; }
  .seat-badge .takeout { font-size: 18px; }
  .seat-badge .ok { color: var(--yellow); font-size: 26px; }
  .shop-name {
    position: absolute; left: 196px; right: 172px; top: 0; bottom: 0;
    display: flex; align-items: center; justify-content: center;
    font-family: "Dela Gothic One", sans-serif;
    font-weight: 400;
    font-size: 84px; line-height: 1; color: var(--yellow);
    letter-spacing: -2px;
    white-space: nowrap;
  }
  .price-badge {
    position: absolute; right: 20px; top: 34px; width: 140px; height: 140px;
    border-radius: 50%; background: var(--black);
    display: flex; flex-direction: column; align-items: center; justify-content: center;
    text-align: center; line-height: 1.05;
    white-space: nowrap;
  }
  .price-badge .dish { color: var(--white); font-size: 26px; }
  .price-badge .price { color: var(--yellow); font-size: 44px; }
  .price-badge .price small { font-size: 24px; }
</style>
</head>
<body>
<div class="canvas">
  <section class="signboard">
    <div class="seat-badge">
      <span class="label">カウンター</span>
      <span class="count">10<small>席</small></span>
      <span class="takeout">持ち帰りも</span>
      <span class="ok">OK!!</span>
    </div>
    <h1 class="shop-name">ゆめポリス</h1>
    <div class="price-badge">
      <span class="dish">カツ丼</span>
      <span class="price">390<small>円</small></span>
    </div>
  </section>
</div>
</body>
</html>
```